Crew Mellow Downgraders and Upgraders Leaflets part 2

Would like to create two double-sided dl card leaflets. This is for an Australian real estate company.

1. Will be to target older people in our area. The down sizers. What do they say when we speak to them – the yard is getting too big, we cant look after the gardens any more. So idea is

Headings could be;
Is Time You Gave Your Mower A Rest?
Give your Mower A Rest
Time To Sell The Lawn Mower?

Call Crew MELLOW. We can Help You

2. Will be to target Upgraders.
Headings could be;
The house too small, kids growing up. Need to find a bigger
Kids Growing Up, Need a Home with More Space?

Call Crew MELLOW, We can Help you

One the back can we have something about Crew Mellow
Please do not forget to include contact numbers for Crew Mellow Members

**We need to Incorporate Crew MELLOW logo, stock photos (not so American) to depict the people of the two cards, and our team photo.
for more info, please see profile pages for Ludo - http://qxvantro.com.au/about/our-team/profile.aspx?sid=41fa9c3d-b7e2-4d10-a6c5-2e9b7f014a83&name=Ludo-Werensky
Tomek - http://qxvantro.com.au/about/our-team/profile.aspx?sid=c803d7e1-9a2f-4c6b-8e15-7d3a60b2f918&name=Tomek-Harbusch

We also have started using this description on our marketing products;
Crew MELLOW is a group of young enthusiastic individuals, living and breathing real estate 24/7. We love what we do and we do what we say. We work from our hearts, and our goal is to create a lasting presence, when we are not present. We hope you too will love experiencing the MELLOW difference.

Industry/Entity Type

Real Estate

```html
<!DOCTYPE html>
<html lang="en">
<head>
<meta charset="utf-8">
<title>Crew Mellow – DL Leaflet</title>
<link rel="stylesheet" href="https://fonts.googleapis.com/css2?family=Kalam:wght@400;700&family=Open+Sans:wght@400;700&display=swap">
<style>
  :root {
    --backdrop: #ff8ab5;
    --paper: #ffffff;
    --ink: #1c1c1c;
    --brand-red: #e2231a;
    --rule-grey: #6d6d6d;
    --frame-grey: #b9bcbf;
    --agency-dark: #3a3a3a;
    --agency-orange: #f6b93a;
    --agency-blue: #3aa6dc;
    --photo-dark: #26262b;
    --photo-light: #eceae8;
  }
  * { box-sizing: border-box; margin: 0; padding: 0; }
  html, body { width: 1200px; height: 900px; overflow: hidden; }
  body {
    background: var(--backdrop);
    font-family: "Kalam", "Comic Sans MS", cursive;
    color: var(--ink);
    position: relative;
  }
  .panel {
    position: absolute;
    top: 37px;
    width: 374px;
    height: 763px;
    background: var(--paper);
    overflow: hidden;
  }
  .panel--front { left: 88px; }
  .panel--back { left: 508px; }

  /* Front */
  .brand {
    position: absolute;
    left: 37px; top: 30px;
    display: flex; align-items: center; gap: 12px;
  }
  .brand__name {
    font-family: "Kalam", cursive;
    font-weight: 700;
    font-size: 40px;
    color: var(--brand-red);
    line-height: 1;
  }
  .brand__mark {
    width: 30px; height: 30px; border-radius: 50%;
    background: var(--brand-red);
  }
  .brand-rule {
    position: absolute; left: 47px; top: 102px;
    width: 280px; height: 2px; background: var(--brand-red);
  }
  .lead {
    position: absolute; left: 0; top: 108px; width: 100%;
    text-align: center; font-size: 15px; line-height: 28px;
  }
  .headline {
    position: absolute; left: 0; top: 183px; width: 100%;
    text-align: center; font-size: 22px; font-weight: 700;
  }
  .cta {
    position: absolute; left: 0; top: 234px; width: 100%;
    text-align: center; font-weight: 700; line-height: 1.05;
  }
  .cta__call { display: block; font-size: 29px; }
  .cta__help { display: block; font-size: 23px; }
  .about {
    position: absolute; left: 58px; top: 322px; width: 258px;
    font-size: 15px; line-height: 21px; font-weight: 700;
    font-variant: small-caps; text-align: justify;
  }
  .team-photo {
    position: absolute; left: 0; top: 538px; width: 100%; height: 225px;
    background: linear-gradient(180deg, var(--paper) 0%, var(--photo-light) 30%, var(--photo-dark) 75%);
  }

  /* Back */
  .member { position: absolute; left: 0; width: 100%; }
  .member--first { top: 76px; }
  .member--second { top: 335px; }
  .member__portrait {
    position: absolute; left: 32px; top: 0;
    width: 74px; height: 74px; border-radius: 50%;
    border: 2px solid var(--frame-grey);
    background: radial-gradient(circle at 50% 40%, #d9d4cf 0%, #9a8f88 55%, #2d2d33 100%);
  }
  .member__rule {
    position: absolute; left: 118px; top: 0;
    width: 2px; height: 212px; background: var(--rule-grey);
  }
  .member__details {
    position: absolute; left: 128px; top: -4px;
    font-size: 15px; line-height: 17px; font-weight: 700;
  }
  .member__name {
    font-size: 21px; font-weight: 400; text-decoration: underline;
    line-height: 24px;
  }
  .member__role { margin-bottom: 19px; }
  .member__label { display: block; }
  .member__value { display: block; letter-spacing: 0.5px; margin-bottom: 19px; }
  .member__value:last-child { margin-bottom: 0; }

  .agency {
    position: absolute; left: 6px; top: 690px; width: 360px; height: 35px;
    display: flex;
  }
  .agency__badge {
    width: 158px; height: 100%; background: var(--paper);
    border-bottom: 4px solid var(--agency-orange);
    display: flex; align-items: center; gap: 6px;
  }
  .agency__square { width: 14px; height: 14px; background: var(--agency-blue); }
  .agency__name {
    font-family: "Kalam", cursive; font-weight: 700; font-size: 15px;
    color: var(--agency-dark);
  }
  .agency__band { flex: 1; background: var(--agency-orange); }
  .agency-contact {
    position: absolute; left: 24px; top: 733px;
    font-family: "Open Sans", sans-serif; font-size: 6.5px;
    color: var(--agency-blue); display: flex; gap: 8px;
  }
  .agency-contact span + span { border-left: 1px solid var(--agency-orange); padding-left: 8px; }
</style>
</head>
<body>
  <section class="panel panel--front">
    <div class="brand">
      <span class="brand__name">Crew Mellow</span>
      <span class="brand__mark"></span>
    </div>
    <div class="brand-rule"></div>
    <p class="lead">The yard is getting too big,<br>We cant look after the gardens any more.</p>
    <h1 class="headline">Give your Mower A Rest</h1>
    <p class="cta">
      <span class="cta__call">Call Crew MELLOW.</span>
      <span class="cta__help">We can Help You.</span>
    </p>
    <p class="about">Crew MELLOW is a group of young enthusiastic individuals, living and breathing real estate 24/7. We love what we do and we do what we say. We work from our hearts, and our goal is to create a lasting presence, when we are not present. We hope you too will love experiencing the MELLOW difference.</p>
    <div class="team-photo" role="img" aria-label="Team photo of four Crew Mellow agents in dark suits"></div>
  </section>

  <section class="panel panel--back">
    <article class="member member--first">
      <div class="member__portrait" role="img" aria-label="Portrait of Ludo Werensky"></div>
      <div class="member__rule"></div>
      <div class="member__details">
        <h2 class="member__name">Ludo Werensky</h2>
        <p class="member__role">Director</p>
        <span class="member__label">Phone</span>
        <span class="member__value">08 9123 4560</span>
        <span class="member__label">Mobile</span>
        <span class="member__value">0400 118 267</span>
        <span class="member__label">Email</span>
        <span class="member__value">ludo@qxvantro.com.au</span>
      </div>
    </article>

    <article class="member member--second">
      <div class="member__portrait" role="img" aria-label="Portrait of Tomek Harbusch"></div>
      <div class="member__rule"></div>
      <div class="member__details">
        <h2 class="member__name">Tomek Harbusch</h2>
        <p class="member__role">Director</p>
        <span class="member__label">Phone</span>
        <span class="member__value">08 9123 4560</span>
        <span class="member__label">Mobile</span>
        <span class="member__value">0400 352 981</span>
        <span class="member__label">Email</span>
        <span class="member__value">tomek@qxvantro.com.au</span>
      </div>
    </article>

    <div class="agency">
      <div class="agency__badge">
        <span class="agency__square"></span>
        <span class="agency__name">Qxvantro Realty</span>
      </div>
      <div class="agency__band"></div>
    </div>
    <p class="agency-contact">
      <span>18 Wattle Street, Belmont WA 6104</span>
      <span>mail@qxvantro.com.au</span>
      <span>9123 4560</span>
      <span>qxvantro.com.au</span>
    </p>
  </section>
</body>
</html>
```